Halvorn Minerals Web Design

Require a Web page design for an international mining and private investment company currently based in Dubai, UAE. I would like to view designs that incorporate our current corporate logo design aimed at communicating global business development/expansion across a diversity of commodities within the mining and investment sectors.

We are a global organisation with global experience and strategy with specific business development focus in Africa, Central and South America.

Target Market(s)

Mining industry, finance, fund raising, brokering, private equity and public stock exchanges.

Industry/Entity Type

Mining

Number of Pages Required

5+ page

Font styles to use
Sans Serif

Colors

Designer to choose colors to be used in the design.

Requirements
Must have
• Corporate logo, description of who we are, what we do, corporate mission, vision & strategy.
Nice to have
• Inclusion of images, photos, interactive maps/graphics and video.

```html
<!DOCTYPE html>
<html lang="en">
<head>
<meta charset="utf-8">
<title>Halvorn Minerals</title>
<link href="https://fonts.googleapis.com/css2?family=Roboto:wght@400;500;700&family=Open+Sans:wght@400;600;700&display=swap" rel="stylesheet">
<style>
:root{
  --gold:#e9b75f;
  --gold-soft:#f5d59a;
  --gold-card:#f4cf8c;
  --dark:#2a2a2a;
  --dark-2:#333539;
  --dark-3:#3e4146;
  --ink:#333;
  --muted:#666;
  --white:#fff;
}
*{box-sizing:border-box;margin:0;padding:0}
html,body{width:1200px;height:3516px;overflow:hidden}
body{font-family:"Open Sans",Arial,sans-serif;color:var(--ink);background:#fff;position:relative}
h1,h2,h3,h4{font-family:"Roboto",Arial,sans-serif}
.sec{position:absolute;left:0;width:1200px}
.abs{position:absolute}

/* header */
.topline{top:0;height:7px;background:var(--dark)}
.header{top:7px;height:87px;background:#fff}
.brand{left:131px;top:22px;display:flex;align-items:center;gap:10px;white-space:nowrap}
.brand-mark{width:40px;height:40px;border-radius:50%;background:var(--gold);flex:none}
.brand-name{font-family:"Roboto",sans-serif;font-weight:700;font-size:19px;color:var(--gold);letter-spacing:.3px}
.nav{right:133px;top:0;display:flex;gap:30px;height:87px;align-items:center;white-space:nowrap}
.nav a{font-family:"Roboto",sans-serif;font-size:14px;color:#333;text-decoration:none;height:87px;line-height:87px;position:relative}
.nav a.active{color:var(--gold)}
.nav a.active::after{content:"";position:absolute;left:0;right:0;bottom:0;height:3px;background:var(--gold)}

/* hero */
.hero{top:94px;height:487px;background:linear-gradient(120deg,#8c8f96 0%,#c9cbd0 35%,#e8e6e2 60%,#b4b8bf 100%)}
.hero-panel{left:136px;top:129px;width:502px;height:187px;background:rgba(40,40,40,.82);padding:22px 28px}
.hero-panel h1{color:var(--gold);font-size:33px;line-height:40px;font-weight:700;text-transform:uppercase}
.hero-panel p{color:#eee;font-size:13px;line-height:19px;margin-top:14px}
.btn-gold{display:inline-block;background:var(--gold-soft);color:#fff;font-family:"Roboto",sans-serif;font-size:13px;font-weight:700;text-transform:uppercase;text-align:center}
.hero .btn-gold{position:absolute;left:136px;top:345px;width:124px;height:37px;line-height:37px}
.slide-arrow{top:230px;width:38px;height:38px;background:rgba(60,60,60,.8)}
.slide-dots{left:580px;top:440px;display:flex;gap:6px}
.slide-dots span{width:18px;height:4px;background:rgba(255,255,255,.6)}
.slide-dots span.on{background:var(--gold)}

/* section headings */
.sec-title{position:absolute;left:0;width:1200px;text-align:center;font-size:27px;font-weight:700;text-transform:uppercase}
.divider{position:absolute;left:560px;width:80px;height:10px}

/* who we are */
.who{top:581px;height:479px}
.who .lede{position:absolute;left:220px;width:760px;top:112px;text-align:center;font-size:13px;line-height:22px;color:var(--muted)}
.card{top:188px;width:295px;height:239px;background:var(--gold-card);padding:12px}
.card-inner{border:2px solid rgba(255,255,255,.8);height:100%;text-align:center;padding:22px 24px;color:#fff}
.card h3{font-size:17px;font-weight:700;text-transform:uppercase;margin-bottom:14px}
.card p{font-size:12px;line-height:18px}
.card .btn-line{display:inline-block;margin-top:22px;border:1px solid rgba(255,255,255,.9);color:#fff;font-size:12px;padding:8px 18px}
.card.dark{background:#333}
.card.dark .card-inner{border-color:#888}

/* business model */
.biz{top:1060px;height:506px;background:linear-gradient(160deg,#4a4a48 0%,#2f2f2e 50%,#5b5347 80%,#3a3835 100%)}
.biz .sec-title{top:62px;color:#fff}
.biz .sub{position:absolute;left:0;width:1200px;top:140px;text-align:center;color:#fff;font-size:13px}
.step{top:211px;width:222px;height:201px;background:rgba(30,30,30,.88);border:1px solid var(--gold);text-align:center;padding:20px 16px}
.step svg{width:52px;height:52px}
.step p{color:#fff;font-family:"Roboto",sans-serif;font-size:13px;line-height:19px;font-weight:500;text-transform:uppercase;margin-top:16px}
.step .pill{position:absolute;left:50%;bottom:-17px;transform:translateX(-50%);width:108px;height:30px;line-height:30px;border-radius:15px;background:var(--gold-soft);color:#fff;font-size:12px;font-weight:700;text-transform:uppercase}

/* mission */
.mission{top:1566px;height:462px}
.mission .kicker{left:134px;top:50px;font-family:"Roboto",sans-serif;font-weight:700;font-size:14px}
.mission h2{position:absolute;left:134px;top:70px;font-size:35px;color:var(--gold);font-weight:500;text-transform:uppercase}
.mission h4{position:absolute;left:134px;top:150px;font-size:14px;font-weight:700;text-transform:uppercase}
.mission .body{left:134px;top:180px;width:515px;font-size:12.5px;line-height:21px;color:#555}
.mission .body p+p{margin-top:14px}
.btn-outline{display:inline-block;border:1px solid var(--gold-soft);color:var(--gold);border-radius:18px;font-size:12px;text-transform:uppercase;text-align:center}
.mission .btn-outline{position:absolute;left:134px;top:368px;width:108px;height:32px;line-height:30px}
.mission .photo-frame{left:710px;top:50px;width:357px;height:355px;border:3px solid var(--gold-soft)}
.mission .photo{left:720px;top:60px;width:337px;height:335px;background:linear-gradient(135deg,#d8d4cc,#9c8f7f 55%,#5d5650)}

/* what we do / vision */
.wwd{top:2028px;height:415px}
.wwd-left{left:0;top:0;width:612px;height:415px;background:linear-gradient(180deg,#3a4049,#23272d 70%,#1c1f24)}
.wwd-left h2{position:absolute;left:0;width:612px;top:85px;text-align:center;color:#fff;font-size:27px;font-weight:700;text-transform:uppercase}
.wwd-left p{position:absolute;left:165px;width:290px;top:140px;text-align:center;color:#fff;font-size:13px;line-height:20px}
.wwd-left .btn-white{position:absolute;left:275px;top:290px;width:106px;height:32px;line-height:32px;background:#fff;border-radius:16px;text-align:center;font-size:13px;color:#333}
.wwd-right{left:612px;top:0;width:588px;height:415px;background:var(--gold-soft);padding:76px 40px 0 32px}
.wwd-right h2{font-size:24px;font-weight:700;text-transform:uppercase;color:#222}
.ticks{list-style:none;margin-top:20px}
.ticks li{display:flex;gap:12px;font-size:13px;line-height:19px;color:#222;margin-bottom:14px;font-weight:600}
.ticks svg{flex:none;width:15px;height:15px;margin-top:2px}
.wwd-right .btn-ghost{display:inline-block;margin-top:16px;border:1px solid #fff;color:#fff;width:98px;height:32px;line-height:30px;text-align:center;font-size:13px}

/* team */
.team{top:2443px;height:454px}
.team-panel{left:134px;top:131px;width:933px;height:253px;background:var(--dark);display:flex}
.member{flex:1;text-align:center;padding-top:22px;border-right:1px solid #555}
.member:last-child{border-right:0}
.member .avatar{width:92px;height:92px;border-radius:50%;margin:0 auto;background:linear-gradient(135deg,#d9d9d9,#a9a9a9);border:3px solid #fff}
.member h3{color:#fff;font-size:17px;font-weight:500;margin-top:18px;text-transform:uppercase;letter-spacing:.5px}
.member .role{color:#ccc;font-size:12px;margin-top:4px}
.socials{display:flex;justify-content:center;gap:7px;margin-top:20px}
.socials span{width:24px;height:24px;background:#fff}

/* contact band */
.cta{top:2897px;height:85px;background:var(--gold-soft)}
.cta .small{left:134px;top:14px;color:#fff;font-size:13px}
.cta .big{left:134px;top:32px;color:#fff;font-family:"Roboto",sans-serif;font-size:25px;font-weight:500;letter-spacing:.5px}
.cta .field{left:776px;top:22px;width:178px;height:38px;border:1px solid #fff;color:#fff;font-size:12px;line-height:36px;padding-left:14px}
.cta .signup{left:956px;top:22px;width:111px;height:38px;background:#fff;color:#333;font-size:14px;line-height:38px;text-align:center}

/* footer */
.footer{top:2982px;height:487px;background:var(--dark-2);color:#ddd}
.footer .brand{left:134px;top:55px}
.footer .brand-name{font-size:22px}
.footer .about{left:134px;top:140px;width:290px;font-size:12.5px;line-height:20px;color:#ddd}
.footer .circles{left:134px;top:266px;display:flex;gap:12px}
.footer .circles span{width:28px;height:28px;border-radius:50%;background:#666}
.footer h4{font-size:19px;font-weight:400;color:#fff}
.links{left:492px;top:50px;width:230px}
.links ul{list-style:none;margin-top:26px}
.links li{font-size:12.5px;border-bottom:1px solid #4d5056;padding:8px 0}
.links li:last-child{border-bottom:0}
.contact{left:804px;top:50px;width:263px}
.addr{display:flex;gap:12px;margin-top:26px;font-size:12.5px;line-height:18px}
.addr svg{flex:none;width:14px;height:18px;margin-top:2px}
.addr+.addr{margin-top:32px}
.contact-bar{left:134px;top:359px;width:933px;height:93px;background:var(--dark-3);display:flex;align-items:center;padding-left:22px;gap:0}
.cb-item{display:flex;align-items:center;gap:14px;width:300px}
.cb-icon{width:46px;height:46px;border:2px solid #ccc;border-radius:4px;display:flex;align-items:center;justify-content:center}
.cb-icon svg{width:22px;height:22px}
.cb-item strong{display:block;font-family:"Roboto",sans-serif;font-size:22px;font-weight:500;color:#fff}
.cb-item small{font-size:13px;color:#ddd}
.copy{top:3469px;height:47px;background:#2a2c30;color:#bbb;font-size:12px;line-height:47px;padding-left:134px}
</style>
</head>
<body>

<div class="sec topline"></div>

<header class="sec header">
  <div class="abs brand"><span class="brand-mark"></span><span class="brand-name">HALVORN MINERALS</span></div>
  <nav class="abs nav">
    <a class="active">Executive Summary</a><a>Team &amp; Experience</a><a>Commercial</a><a>Business Model</a><a>Strategy</a>
  </nav>
</header>

<section class="sec hero" role="img" aria-label="Photo of business team meeting around a table with charts">
  <div class="abs hero-panel">
    <h1>Halvorn Minerals<br>Services</h1>
    <p>The Halvorn Minerals team have provided mining &amp; drilling services to some of the largest mining. The Halvorn Minerals team have provided mining.</p>
  </div>
  <span class="btn-gold">Read More</span>
  <div class="abs slide-arrow" style="left:0"><svg viewBox="0 0 38 38"><path d="M22 13l-6 6 6 6" stroke="#fff" stroke-width="2" fill="none"/></svg></div>
  <div class="abs slide-arrow" style="right:0"><svg viewBox="0 0 38 38"><path d="M16 13l6 6-6 6" stroke="#fff" stroke-width="2" fill="none"/></svg></div>
  <div class="abs slide-dots"><span class="on"></span><span></span></div>
</section>

<section class="sec who">
  <h2 class="sec-title" style="top:55px">Who We Are</h2>
  <svg class="divider" style="top:98px" viewBox="0 0 80 10"><line x1="0" y1="5" x2="80" y2="5" stroke="#e9b75f"/><rect x="36" y="1" width="8" height="8" transform="rotate(45 40 5)" fill="#e9b75f"/></svg>
  <p class="lede">Lorem Ipsum is simply dummy text of the printing and typesetting industry. Lorem Ipsum has been the industry's standard dummy text ever since the 1500s, when an unknown printer took a galley of type and.</p>
  <div class="abs card" style="left:134px"><div class="card-inner"><h3>Team &amp; Experience</h3><p>The management team of Halvorn Minerals have a significant amount of experience in large mine developments.</p><span class="btn-line">Read More »</span></div></div>
  <div class="abs card dark" style="left:455px"><div class="card-inner"><h3>Strategy</h3><p>Targeting multiple growth options &amp; an asset portfolio capable of delivering value at every stage of the development pipeline.</p><span class="btn-line">Read More »</span></div></div>
  <div class="abs card" style="left:774px"><div class="card-inner"><h3>Business Model</h3><p>Identify &amp; secure techno-economic and commercially attractive projects. Deliver key milestones &amp; monetise at appropriate value points.</p><span class="btn-line">Read More »</span></div></div>
</section>

<section class="sec biz" role="img" aria-label="Dark photo of a mining site with heavy machinery">
  <h2 class="sec-title">Business Model</h2>
  <svg class="divider" style="top:108px" viewBox="0 0 80 10"><line x1="0" y1="5" x2="80" y2="5" stroke="#e9b75f"/><rect x="36" y="1" width="8" height="8" transform="rotate(45 40 5)" fill="#e9b75f"/></svg>
  <p class="sub">Value creation through discovery, de-risking &amp; transactions</p>
  <div class="abs step" style="left:134px">
    <svg viewBox="0 0 52 52" fill="none" stroke="#fff" stroke-width="2.5"><rect x="6" y="8" width="36" height="30" rx="2"/><circle cx="18" cy="20" r="5"/><path d="M10 34c2-6 14-6 16 0"/><circle cx="40" cy="38" r="8" fill="#2a2a2a"/><path d="M36 38l3 3 5-6"/></svg>
    <p>Identify &amp; secure techno-economic and commercially attractive projects.</p><span class="pill">Read More</span></div>
  <div class="abs step" style="left:370px">
    <svg viewBox="0 0 52 52" fill="none" stroke="#fff" stroke-width="2.5"><circle cx="34" cy="16" r="8"/><path d="M4 34h12l8 4h10l10-8M4 44h14l10 2 16-10"/></svg>
    <p>Deliver key milestones &amp; monetise at appropriate value points</p><span class="pill">Read More</span></div>
  <div class="abs step" style="left:607px">
    <svg viewBox="0 0 52 52" fill="#fff"><path d="M10 26a16 16 0 0 1 32 0v3H10z"/><rect x="24" y="6" width="4" height="12"/><path d="M16 33h20l-4 12H20z"/></svg>
    <p>Develop JV, divest<br>or spin out</p><span class="pill">Read More</span></div>
  <div class="abs step" style="left:846px">
    <svg viewBox="0 0 52 52" fill="none" stroke="#fff" stroke-width="2.5"><rect x="8" y="4" width="30" height="40" rx="2"/><path d="M14 14h18M14 22h18M14 30h10"/><circle cx="38" cy="38" r="8" fill="#2a2a2a"/><path d="M34 38l3 3 5-6"/></svg>
    <p>One or two "focus projects" at any time offering the highest value potential</p><span class="pill">Read More</span></div>
</section>

<section class="sec mission">
  <span class="abs kicker">OUR</span>
  <h2>Corporate Mission</h2>
  <h4>Lorem Ipsum is simply dummy text of the printing</h4>
  <div class="abs body">
    <p>It is a long established fact that a reader will be distracted by the readable content of a page when looking at its layout. The point of using Lorem Ipsum is that it has a more-or-less normal distribution of letters, as opposed to using 'Content here, content here', making it look like readable English. Many desktop publishing packages and web page</p>
    <p>It is a long established fact that a reader will be distracted by the readable content of a page when looking at its layout. The point of using Lorem Ipsum is that it has.</p>
  </div>
  <span class="btn-outline">Read More</span>
  <div class="abs photo-frame"></div>
  <div class="abs photo" role="img" aria-label="Photo of a professional working on a laptop in a bright office"></div>
</section>

<section class="sec wwd">
  <div class="abs wwd-left" role="img" aria-label="Photo of a city skyline at dusk">
    <h2>What We Do</h2>
    <p>It is a long established fact that a reader will be distracted by the readable content of a page when looking at its layout. The point of using Lorem Ipsum is that it has a more-or-less normal distribution of letters, as opposed to using 'Content here, content here'.</p>
    <span class="btn-white">Read More</span>
  </div>
  <div class="abs wwd-right">
    <h2>Vision &amp; Strategy</h2>
    <ul class="ticks">
      <li><svg viewBox="0 0 15 15"><circle cx="7.5" cy="7.5" r="7.5" fill="#222"/><path d="M4 7.5l2.5 2.5 4.5-5" stroke="#f5d59a" stroke-width="1.8" fill="none"/></svg>Halvorn Minerals has committed to maintaining &amp; establishing a global presence in the global mining sector in 2018 with a specific focus on South America, Central America &amp; Africa.</li>
      <li><svg viewBox="0 0 15 15"><circle cx="7.5" cy="7.5" r="7.5" fill="#222"/><path d="M4 7.5l2.5 2.5 4.5-5" stroke="#f5d59a" stroke-width="1.8" fill="none"/></svg>Halvorn Minerals have the expertise needed to take on small, medium or large scale mining projects through our relationships &amp; extended network of mining professionals.</li>
    </ul>
    <span class="btn-ghost">Read More</span>
  </div>
</section>

<section class="sec team">
  <h2 class="sec-title" style="top:55px">Team &amp; Experience</h2>
  <svg class="divider" style="top:98px" viewBox="0 0 80 10"><line x1="0" y1="5" x2="80" y2="5" stroke="#e9b75f"/><rect x="36" y="1" width="8" height="8" transform="rotate(45 40 5)" fill="#e9b75f"/></svg>
  <div class="abs team-panel">
    <div class="member"><div class="avatar" role="img" aria-label="Portrait of the chairman"></div><h3>Martin Ashgrove</h3><p class="role">Chairman</p><div class="socials"><span></span><span></span><span></span><span></span></div></div>
    <div class="member"><div class="avatar" role="img" aria-label="Portrait of the CEO"></div><h3>Daniel Orme</h3><p class="role">CEO</p><div class="socials"><span></span><span></span><span></span><span></span></div></div>
    <div class="member"><div class="avatar" role="img" aria-label="Portrait of the CFO"></div><h3>Clara Vennet</h3><p class="role">CFO</p><div class="socials"><span></span><span></span><span></span><span></span></div></div>
    <div class="member"><div class="avatar" role="img" aria-label="Portrait of the technical director"></div><h3>Rafael Quinto</h3><p class="role">Technical Director</p><div class="socials"><span></span><span></span><span></span><span></span></div></div>
  </div>
</section>

<section class="sec cta">
  <span class="abs small">Have Any Questions</span>
  <span class="abs big">Don't Hesitate to contact us and get the solution</span>
  <span class="abs field">Enter your e-mail address</span>
  <span class="abs signup">Sign Up</span>
</section>

<footer class="sec footer">
  <div class="abs brand"><span class="brand-mark" style="background:#fff"></span><span class="brand-name" style="color:#fff">HALVORN MINERALS</span></div>
  <p class="abs about">There are many variations of the dummy passages of Lorem Ipsum dummy that an available but, of Lorem Ipsum dummy that an available but.</p>
  <div class="abs circles"><span></span><span></span><span></span><span></span></div>
  <div class="abs links">
    <h4>Use Link</h4>
    <ul><li>Executive Summary</li><li>Team &amp; Experience</li><li>Commercial</li><li>Business Model</li><li>Strategy</li></ul>
  </div>
  <div class="abs contact">
    <h4>Contact Info</h4>
    <div class="addr"><svg viewBox="0 0 14 18"><path d="M7 0a7 7 0 0 0-7 7c0 5 7 11 7 11s7-6 7-11a7 7 0 0 0-7-7zm0 10a3 3 0 1 1 0-6 3 3 0 0 1 0 6z" fill="#fff"/></svg><span>Dubai, UAE<br>Halvorn Minerals FZ LLC<br>Suite 210, Tower 3, Crescent Business Park, Harbour Quarter, Dubai, UAE.</span></div>
    <div class="addr"><svg viewBox="0 0 14 18"><path d="M7 0a7 7 0 0 0-7 7c0 5 7 11 7 11s7-6 7-11a7 7 0 0 0-7-7zm0 10a3 3 0 1 1 0-6 3 3 0 0 1 0 6z" fill="#fff"/></svg><span>Guinea, West Africa<br>Rue des Palmiers, Quartier Nord, Immeuble 12, BP: 4410</span></div>
  </div>
  <div class="abs contact-bar">
    <div class="cb-item"><span class="cb-icon"><svg viewBox="0 0 24 24"><path d="M6 2l4 4-2 3c1 3 4 6 7 7l3-2 4 4-3 4C10 22 2 14 2 5z" fill="#fff"/></svg></span><div><strong>Phone :</strong><small>+224 600 000 123 / +61 400 000 456</small></div></div>
    <div class="cb-item"><span class="cb-icon"><svg viewBox="0 0 24 24"><path d="M22 2L2 10l8 3 3 9z" fill="#fff"/></svg></span><div><strong>Post :</strong><small>PO Box 100234</small></div></div>
    <div class="cb-item"><span class="cb-icon"><svg viewBox="0 0 24 24"><rect x="2" y="5" width="20" height="14" fill="#fff"/><path d="M2 5l10 8 10-8" stroke="#3e4146" stroke-width="1.8" fill="none"/></svg></span><div><strong>Mail :</strong><small>info@halvornminerals.com</small></div></div>
  </div>
</footer>

<div class="sec copy">© 2018 Halvorn Minerals Services. All Rights Reserved.</div>

</body>
</html>
```